Arranging Your Money Matters PowerPoint

I need to create a PowerPoint presentation that describes our product and demonstrates how to use it. Our product is an organizational binder that helps clients put all of their important financial and legal documents in one place. I will upload all forms that will be in the binder, as well as our logo and the table of contents. Initially, I think it makes sense to have a slide for every section in the table of contents. There are 18 sections, so I would envision approximately 20 slides.
I would like the first slide to have a deep blue background, with the logo in a shiny gold if possible.
At some point in the presentation slides or throughout, I would like to have the WorkLoop logo, and I would like it to have the following contact information:

Deirdre Valcourt
arrangingyourmoneymatters@mailbox-example.net

I have uploaded the forms that will be in the binder, and each file has a number at the beginning of the file name so they are in order of how they go into the binder. The table of contents is the second file, and will give you an idea of some discussion points.

I have uploaded a photo of the front of a binder to give an idea for color of the main slide and logo. However, please note that the NEW logo has been uploaded. The binder in the picture does not have the correct logo.

Target Market(s)

Financial Advisors, Accountants, Attorneys, and clients of them

Industry/Entity Type

Financial Planning

Requirements
Must have
• 1. I think we can condense the Table of Contents onto one slide by just listing the heading for each section (i.e. Survivor Instructions, Important Contacts, etc.) but leaving out the detail for each section. It will not be necessary to have page numbers for the items in the table of contents.
• 2. After the table of contents slide, I would like to have a slide for each section heading, and the detail for each heading on that slide. The slides would be:
• - title slide
• - Opening Letter
• - Table of Contents
• - Survivor Instructions
• - Important Contacts
• - Information Access
• - Asset Statements
• - Loan Statements
• - Household Billing Statements
• - Education Planning
• - Insurance Inventory
• - Estate Planning
• - Powers of Attorney
• - Family Legal
• - Business Formations
• - Healthcare
• - Future Income
• - Taxes
• - Personal History
• - Resources
• - Important Documents
• Each of these slides would have the content listed under that heading in the table of contents.
• The last slide should say something like "Thank You!" and have:
• 1. The Arrange Your Money Matters logo
• 2. The WorkLoop logo
• 3. Deirdre Valcourt
• 4. arrangeyourmoneymatters@mailbox-example.net
Nice to have
• Colorful visuals or graphics
Should not have
• Slides with too much information on them

```html
<!DOCTYPE html>
<html lang="en">
<head>
<meta charset="utf-8">
<title>Arranging Your Money Matters – Slide Overview</title>
<link href="https://fonts.googleapis.com/css2?family=Cinzel:wght@400;600&family=Open+Sans:wght@400;600;700&display=swap" rel="stylesheet">
<style>
:root{
  --navy:#0d2a5c;
  --navy-deep:#071a3d;
  --navy-mid:#123a78;
  --blue:#1a63c4;
  --sky:#9fb6d9;
  --pale:#cfdaea;
  --gold:#d9ad4a;
  --peach:#fde3c9;
  --ink:#3a3a3a;
  --band:#d7d7d7;
}
*{box-sizing:border-box}
html,body{margin:0;width:786px;height:1200px;overflow:hidden}
body{background:var(--peach);position:relative;font-family:'Open Sans',sans-serif;color:var(--ink)}
.slide{position:absolute;width:250px;height:142px;background:#fff;overflow:hidden}
.slide.dark{background:radial-gradient(ellipse at 50% 40%,var(--navy-mid),var(--navy-deep))}
.heading{position:absolute;left:0;top:7px;display:flex;align-items:center;gap:4px;font-weight:700;font-size:9.5px;color:var(--navy);margin:0}
.heading svg{width:9px;height:11px;display:block}
.icon{position:absolute;left:26px;top:36px;width:60px;height:60px;border-radius:50%;
  background:radial-gradient(circle at 45% 40%,#ffffff 40%,#e2e2e2);box-shadow:0 1px 3px rgba(0,0,0,.25)}
.icon::after{content:"";position:absolute;inset:16px;border-radius:8px;background:linear-gradient(135deg,#5a5a5a,#222);opacity:.85}
.points{position:absolute;left:118px;margin:0;padding:0;list-style:none;font-size:5px;display:flex;flex-direction:column}
.points li{position:relative;padding-left:10px;line-height:1.35}
.points li::before{content:"";position:absolute;left:0;top:1px;width:5px;height:5px;border-radius:50%;background:var(--navy)}
.points li:nth-child(3)::before{background:var(--blue)}
.points li:nth-child(4)::before{background:var(--sky)}
.points li:nth-child(n+5)::before{background:var(--pale)}
.points .sub{display:block;font-size:3.4px;color:#666}
.points .group{color:var(--blue)}
.points .inner{list-style:none;padding-left:8px;margin:1px 0}
.points .inner li{padding-left:7px}
.points .inner li::before{width:2px;height:2px;top:2px;background:#333}
.points .link{color:var(--blue);text-decoration:underline}
.footer{position:absolute;left:0;right:0;bottom:0;height:9px;background:var(--band)}
.footer .contact{position:absolute;left:3px;top:1px;display:flex;align-items:center;gap:2px;font-size:2.8px;line-height:1.1}
.footer .mark{width:6px;height:6px;background:var(--navy)}
.footer .band{position:absolute;left:108px;top:0;width:38px;height:9px;background:var(--navy);transform:skewX(-30deg)}
.footer .band::after{content:"";position:absolute;left:15px;top:2px;width:5px;height:5px;border-radius:50%;border:.6px solid var(--gold)}
.footer .pg{position:absolute;right:8px;top:2px;font-size:4px;color:#777}
.brand{font-family:'Cinzel',serif;font-weight:400;color:var(--gold);text-align:center;letter-spacing:.5px;line-height:1.15}
.brand-ring{border:1.5px solid var(--gold);border-radius:50%;margin:0 auto}
.two{display:flex;gap:14px;position:absolute;left:118px}
.two .points{position:static}
</style>
</head>
<body>

<svg width="0" height="0" style="position:absolute">
  <symbol id="chev" viewBox="0 0 9 11"><rect width="9" height="11" fill="#0d2a5c"/><path d="M2.5 2l3.5 3.5-3.5 3.5" stroke="#fff" stroke-width="1.6" fill="none"/></symbol>
</svg>

<!-- 1 Title -->
<section class="slide dark" style="left:7px;top:8px">
  <div style="position:absolute;left:0;right:0;top:28px">
    <div class="brand-ring" style="width:44px;height:44px"></div>
    <p class="brand" style="font-size:14px;margin:8px 0 0">ARRANGING YOUR<br>MONEY MATTERS</p>
  </div>
  <span style="position:absolute;right:8px;bottom:4px;font-size:3.5px;color:#8aa">1</span>
</section>

<!-- 2 TOC -->
<section class="slide" style="left:266px;top:8px">
  <div class="dark" style="position:absolute;left:0;top:0;width:110px;height:142px;background:radial-gradient(ellipse at 50% 40%,var(--navy-mid),var(--navy-deep))">
    <div style="position:absolute;left:0;right:0;top:40px">
      <div class="brand-ring" style="width:18px;height:18px"></div>
      <p class="brand" style="font-size:6px;margin:4px 0 0">ARRANGING YOUR<br>MONEY MATTERS</p>
      <p class="brand" style="font-size:6px;margin:10px 0 0;letter-spacing:.8px">TABLE OF CONTENTS</p>
    </div>
  </div>
  <ol style="position:absolute;left:114px;top:17px;margin:0;padding:0;list-style:none;font-size:3.4px;width:126px;color:var(--blue)">
    <li style="border-bottom:.3px solid #ccc;line-height:1.75"><b style="color:#333">01</b>&nbsp; Survivor Instructions</li>
    <li style="border-bottom:.3px solid #ccc;line-height:1.75"><b style="color:#333">02</b>&nbsp; Important Contacts</li>
    <li style="border-bottom:.3px solid #ccc;line-height:1.75"><b style="color:#333">03</b>&nbsp; Information Access</li>
    <li style="border-bottom:.3px solid #ccc;line-height:1.75"><b style="color:#333">04</b>&nbsp; Asset Statements</li>
    <li style="border-bottom:.3px solid #ccc;line-height:1.75"><b style="color:#333">05</b>&nbsp; Loan Statements</li>
    <li style="border-bottom:.3px solid #ccc;line-height:1.75"><b style="color:#333">06</b>&nbsp; Household Billing Statements</li>
    <li style="border-bottom:.3px solid #ccc;line-height:1.75"><b style="color:#333">07</b>&nbsp; Education Planning</li>
    <li style="border-bottom:.3px solid #ccc;line-height:1.75"><b style="color:#333">08</b>&nbsp; Insurance Inventory</li>
    <li style="border-bottom:.3px solid #ccc;line-height:1.75"><b style="color:#333">09</b>&nbsp; Estate Planning</li>
    <li style="border-bottom:.3px solid #ccc;line-height:1.75"><b style="color:#333">10</b>&nbsp; Powers of Attorney</li>
    <li style="border-bottom:.3px solid #ccc;line-height:1.75"><b style="color:#333">11</b>&nbsp; Family Legal</li>
    <li style="border-bottom:.3px solid #ccc;line-height:1.75"><b style="color:#333">12</b>&nbsp; Business Formations</li>
    <li style="border-bottom:.3px solid #ccc;line-height:1.75"><b style="color:#333">13</b>&nbsp; Healthcare</li>
    <li style="border-bottom:.3px solid #ccc;line-height:1.75"><b style="color:#333">14</b>&nbsp; Future Income</li>
    <li style="border-bottom:.3px solid #ccc;line-height:1.75"><b style="color:#333">15</b>&nbsp; Taxes</li>
    <li style="border-bottom:.3px solid #ccc;line-height:1.75"><b style="color:#333">16</b>&nbsp; Personal History</li>
    <li style="border-bottom:.3px solid #ccc;line-height:1.75"><b style="color:#333">17</b>&nbsp; Resources</li>
    <li style="border-bottom:.3px solid #ccc;line-height:1.75"><b style="color:#333">18</b>&nbsp; Important Documents</li>
  </ol>
  <span style="position:absolute;right:8px;bottom:4px;font-size:3.5px;color:#999">2</span>
</section>

<!-- 3 Opening letter -->
<section class="slide" style="left:524px;top:8px">
  <h2 class="heading"><svg><use href="#chev"/></svg>Opening Letter</h2>
  <div style="position:absolute;left:13px;right:10px;top:24px;font-size:3.2px;line-height:1.35">
    <p style="margin:0 0 2px;font-weight:700">Dear Friends,</p>
    <p style="margin:0 0 3px">This binder is one way to simplify and organize your financial and legal papers. It will help you now, and it will be especially helpful for your family if you are ever unable to act. Keeping papers together lightens the load on loved ones during a hard time.</p>
    <p style="margin:0 0 3px">I recommend that you take as much time as needed to complete the binder. It matters just as much that you set a time to keep it current, and I suggest the following:</p>
    <div style="display:flex;gap:2px;background:#e4e4e4;padding:3px;font-size:2.6px;color:var(--blue)">
      <div style="flex:1">February 1 annually: update account statements, loan statements and household billing records.</div>
      <div style="flex:1;background:#cfcfcf;padding:1px">June 1 annually: update benefit estimates and tax returns.</div>
      <div style="flex:1">December 1, every three years: review estate plan, beneficiaries and powers of attorney.</div>
    </div>
    <p style="margin:3px 0 0">It is unlikely that any of these days will need more than one hour of work. Don't forget to tell your family or a trusted friend where the binder is kept.</p>
    <p style="margin:2px 0 0;text-align:right;font-weight:700">Sincerely,<br>Deirdre Valcourt</p>
  </div>
  <footer class="footer"><div class="contact"><span class="mark"></span><span>WorkLoop · Deirdre Valcourt<br>arrangingyourmoneymatters@mailbox-example.net</span></div><span class="band"></span><span class="pg">3</span></footer>
</section>

<!-- 4 Survivor -->
<section class="slide" style="left:7px;top:158px">
  <h2 class="heading"><svg><use href="#chev"/></svg>Survivor Instructions</h2>
  <div class="icon" role="img" aria-label="Open book icon"></div>
  <ul class="points" style="top:58px;gap:9px"><li>Letter of Instruction</li><li>Letter to Children</li></ul>
  <footer class="footer"><div class="contact"><span class="mark"></span><span>WorkLoop · Deirdre Valcourt<br>arrangingyourmoneymatters@mailbox-example.net</span></div><span class="band"></span><span class="pg">4</span></footer>
</section>

<!-- 5 Contacts -->
<section class="slide" style="left:266px;top:158px">
  <h2 class="heading"><svg><use href="#chev"/></svg>Important Contacts</h2>
  <div class="icon" role="img" aria-label="Address book icon"></div>
  <ul class="points" style="top:22px">
    <li class="group">Professional Contacts
      <ul class="inner" style="color:var(--ink)"><li>Financial Advisor</li><li>Estate Attorney</li><li>CPA or Accountant</li><li>Insurance Agent</li><li>Business Relationships</li><li>Primary Care Physician</li><li>Dentist</li></ul></li>
    <li class="group" style="margin-top:0">Personal Contacts
      <ul class="inner" style="color:var(--ink)"><li>Relatives</li><li>Friends</li></ul></li>
  </ul>
  <footer class="footer"><div class="contact"><span class="mark"></span><span>WorkLoop · Deirdre Valcourt<br>arrangingyourmoneymatters@mailbox-example.net</span></div><span class="band"></span><span class="pg">5</span></footer>
</section>

<!-- 6 Info access -->
<section class="slide" style="left:524px;top:158px">
  <h2 class="heading"><svg><use href="#chev"/></svg>Information Access</h2>
  <div class="icon" role="img" aria-label="Envelope with key icon"></div>
  <ul class="points" style="top:22px;gap:11px"><li>Online accounts, passwords</li><li>Online debits, billpay</li><li>Safe Deposit boxes<span class="sub">(identify authorized signer or co-owner)</span></li><li>Keys, electronic codes</li><li>Safe combination</li></ul>
  <footer class="footer"><div class="contact"><span class="mark"></span><span>WorkLoop · Deirdre Valcourt<br>arrangingyourmoneymatters@mailbox-example.net</span></div><span class="band"></span><span class="pg">6</span></footer>
</section>

<!-- 7 Assets -->
<section class="slide" style="left:7px;top:307px">
  <h2 class="heading"><svg><use href="#chev"/></svg>Asset Statements</h2>
  <div class="icon" role="img" aria-label="Calculator and bank chart icon"></div>
  <ul class="points" style="top:19px;gap:11px"><li>Bank Accounts</li><li>Brokerage Accounts</li><li>Retirement Accounts (401k, IRA, Roth)</li><li>EE Bonds or stock certificates</li><li>Annuities</li><li>Stock Options</li></ul>
  <footer class="footer"><div class="contact"><span class="mark"></span><span>WorkLoop · Deirdre Valcourt<br>arrangingyourmoneymatters@mailbox-example.net</span></div><span class="band"></span><span class="pg">7</span></footer>
</section>

<!-- 8 Loans -->
<section class="slide" style="left:266px;top:307px">
  <h2 class="heading"><svg><use href="#chev"/></svg>Loan Statements</h2>
  <div class="icon" role="img" aria-label="Statement and card icon"></div>
  <ul class="points" style="top:27px;gap:11px"><li>Mortgage</li><li>Auto Loans</li><li>Credit Cards</li><li>Home Equity</li><li>Recreational vehicle, boat</li></ul>
  <footer class="footer"><div class="contact"><span class="mark"></span><span>WorkLoop · Deirdre Valcourt<br>arrangingyourmoneymatters@mailbox-example.net</span></div><span class="band"></span><span class="pg">8</span></footer>
</section>

<!-- 9 Household -->
<section class="slide" style="left:524px;top:307px">
  <h2 class="heading"><svg><use href="#chev"/></svg>Household Billing Statements</h2>
  <div class="icon" role="img" aria-label="Utility bill and faucet icon"></div>
  <div class="two" style="top:37px">
    <ul class="points" style="gap:9px;font-size:4.2px"><li>Water/sewer</li><li>Trash/recycling</li><li>Natural Gas/Propane</li><li>Electric</li><li>Phone/Internet/Television</li></ul>
    <ul class="points" style="gap:9px;font-size:4.2px"><li>Mobile Phone</li><li>Newspaper/Magazines</li><li style="--x:0">Online subscriptions</li><li>Property tax</li></ul>
  </div>
  <footer class="footer"><div class="contact"><span class="mark"></span><span>WorkLoop · Deirdre Valcourt<br>arrangingyourmoneymatters@mailbox-example.net</span></div><span class="band"></span><span class="pg">9</span></footer>
</section>

<!-- 10 Education -->
<section class="slide" style="left:7px;top:456px">
  <h2 class="heading"><svg><use href="#chev"/></svg>Education Planning</h2>
  <div class="icon" role="img" aria-label="Hands holding a brain icon"></div>
  <ul class="points" style="top:55px;gap:9px"><li>Statements <span style="font-size:3.6px">(529, Coverdell, Custodial)</span></li><li>Education Reports</li></ul>
  <footer class="footer"><div class="contact"><span class="mark"></span><span>WorkLoop · Deirdre Valcourt<br>arrangingyourmoneymatters@mailbox-example.net</span></div><span class="band"></span><span class="pg">10</span></footer>
</section>

<!-- 11 Insurance -->
<section class="slide" style="left:266px;top:456px">
  <h2 class="heading"><svg><use href="#chev"/></svg>Insurance Inventory</h2>
  <div class="icon" role="img" aria-label="Umbrella icon"></div>
  <ul class="points" style="top:20px;gap:11px"><li>Life Insurance</li><li>Disability Insurance</li><li>Long Term Care Insurance</li><li>Property/Casualty Insurance</li><li>Umbrella Liability Insurance</li><li>Video inventory of assets <span style="font-size:3.4px">(USB flash drive or SD card)</span></li></ul>
  <footer class="footer"><div class="contact"><span class="mark"></span><span>WorkLoop · Deirdre Valcourt<br>arrangingyourmoneymatters@mailbox-example.net</span></div><span class="band"></span><span class="pg">11</span></footer>
</section>

<!-- 12 Estate -->
<section class="slide" style="left:524px;top:456px">
  <h2 class="heading"><svg><use href="#chev"/></svg>Estate Planning</h2>
  <div class="icon" role="img" aria-label="House plan on easel icon"></div>
  <ul class="points" style="top:13px;gap:11px"><li>Letter of Intent (sample)</li><li>Will</li><li>Trust</li><li>Firearms Trust</li><li>Documentation of expensive items and values (guns, jewelry)</li><li>Funeral preplanning</li></ul>
  <footer class="footer"><div class="contact"><span class="mark"></span><span>WorkLoop · Deirdre Valcourt<br>arrangingyourmoneymatters@mailbox-example.net</span></div><span class="band"></span><span class="pg">12</span></footer>
</section>

<!-- 13 POA -->
<section class="slide" style="left:7px;top:606px">
  <h2 class="heading"><svg><use href="#chev"/></svg>Powers of Attorney</h2>
  <div class="icon" role="img" aria-label="Gavel icon"></div>
  <ul class="points" style="top:54px;gap:14px"><li>Financial POA</li><li>Healthcare POA</li></ul>
  <footer class="footer"><div class="contact"><span class="mark"></span><span>WorkLoop · Deirdre Valcourt<br>arrangingyourmoneymatters@mailbox-example.net</span></div><span class="band"></span><span class="pg">13</span></footer>
</section>

<!-- 14 Family legal -->
<section class="slide" style="left:266px;top:606px">
  <h2 class="heading"><svg><use href="#chev"/></svg>Family Legal</h2>
  <div class="icon" role="img" aria-label="Family under a roof icon"></div>
  <ul class="points" style="top:46px;gap:11px"><li>Divorce decrees</li><li>Powers of Attorney for children over 18</li><li>Powers of Attorney for whom you are agent</li></ul>
  <footer class="footer"><div class="contact"><span class="mark"></span><span>WorkLoop · Deirdre Valcourt<br>arrangingyourmoneymatters@mailbox-example.net</span></div><span class="band"></span><span class="pg">14</span></footer>
</section>

<!-- 15 Business -->
<section class="slide" style="left:524px;top:606px">
  <h2 class="heading"><svg><use href="#chev"/></svg>Business Formations</h2>
  <div class="icon" role="img" aria-label="Briefcase icon"></div>
  <ul class="points" style="top:50px;gap:11px"><li>Limited Liability Companies</li><li>Family Limited Partnerships</li><li>Firearms Trusts</li></ul>
  <footer class="footer"><div class="contact"><span class="mark"></span><span>WorkLoop · Deirdre Valcourt<br>arrangingyourmoneymatters@mailbox-example.net</span></div><span class="band"></span><span class="pg">15</span></footer>
</section>

<!-- 16 Healthcare -->
<section class="slide" style="left:7px;top:754px">
  <h2 class="heading"><svg><use href="#chev"/></svg>Healthcare</h2>
  <div class="icon" role="img" aria-label="Doctor icon"></div>
  <ul class="points" style="top:40px;gap:11px;letter-spacing:-.1px"><li>Photocopies of Insurance Cards</li><li>List Doctors, Prescriptions, Pharmacies</li><li>List of allergies</li><li>List of known medical conditions</li></ul>
  <footer class="footer"><div class="contact"><span class="mark"></span><span>WorkLoop · Deirdre Valcourt<br>arrangingyourmoneymatters@mailbox-example.net</span></div><span class="band"></span><span class="pg">16</span></footer>
</section>

<!-- 17 Future income -->
<section class="slide" style="left:266px;top:754px">
  <h2 class="heading"><svg><use href="#chev"/></svg>Future Income</h2>
  <div class="icon" role="img" aria-label="Hand holding coin icon"></div>
  <ul class="points" style="top:52px;gap:12px"><li>Pension Benefit Estimates</li><li>Social Security Benefit Estimates<br><span class="link">(www.benefits-example.gov/account)</span></li></ul>
  <footer class="footer"><div class="contact"><span class="mark"></span><span>WorkLoop · Deirdre Valcourt<br>arrangingyourmoneymatters@mailbox-example.net</span></div><span class="band"></span><span class="pg">17</span></footer>
</section>

<!-- 18 Taxes -->
<section class="slide" style="left:524px;top:754px">
  <h2 class="heading"><svg><use href="#chev"/></svg>Taxes</h2>
  <div class="icon" role="img" aria-label="Tax form icon"></div>
  <ul class="points" style="top:55px;gap:11px"><li>Federal Tax Return</li><li>State Tax Return</li></ul>
  <footer class="footer"><div class="contact"><span class="mark"></span><span>WorkLoop · Deirdre Valcourt<br>arrangingyourmoneymatters@mailbox-example.net</span></div><span class="band"></span><span class="pg">18</span></footer>
</section>

<!-- 19 Personal history -->
<section class="slide" style="left:7px;top:904px">
  <h2 class="heading"><svg><use href="#chev"/></svg>Personal History</h2>
  <div class="icon" role="img" aria-label="Résumé document icon"></div>
  <ul class="points" style="top:66px"><li>Personal History</li></ul>
  <footer class="footer"><div class="contact"><span class="mark"></span><span>WorkLoop · Deirdre Valcourt<br>arrangingyourmoneymatters@mailbox-example.net</span></div><span class="band"></span><span class="pg">19</span></footer>
</section>

<!-- 20 Resources -->
<section class="slide" style="left:266px;top:904px">
  <h2 class="heading"><svg><use href="#chev"/></svg>Resources</h2>
  <div class="icon" role="img" aria-label="Magnifying glass icon"></div>
  <ul class="points" style="top:58px;gap:11px"><li>Recommended Reading</li><li>Links to helpful websites</li></ul>
  <footer class="footer"><div class="contact"><span class="mark"></span><span>WorkLoop · Deirdre Valcourt<br>arrangingyourmoneymatters@mailbox-example.net</span></div><span class="band"></span><span class="pg">20</span></footer>
</section>

<!-- 21 Important documents -->
<section class="slide" style="left:524px;top:904px">
  <h2 class="heading"><svg><use href="#chev"/></svg>Important Documents</h2>
  <div class="icon" role="img" aria-label="Signed document icon"></div>
  <div class="two" style="top:34px;left:96px;gap:12px">
    <ul class="points" style="gap:9px;font-size:4px;width:80px"><li>Photocopies of Drivers' Licenses</li><li>Birth Certificates</li><li>Social Security Cards</li><li>Photos of Passports</li><li>Names of all children, SSNs, DOBs, addresses, phone</li></ul>
    <ul class="points" style="font-size:4px;gap:2px"><li>Deeds &amp; Titles<ul class="inner"><li>Home</li><li>Auto</li></ul></li><li>Appraisals and Photos<ul class="inner"><li>Jewelry</li><li>Art</li><li>Firearms</li></ul></li></ul>
  </div>
  <footer class="footer"><div class="contact"><span class="mark"></span><span>WorkLoop · Deirdre Valcourt<br>arrangingyourmoneymatters@mailbox-example.net</span></div><span class="band"></span><span class="pg">21</span></footer>
</section>

<!-- 22 Thank you -->
<section class="slide dark" style="left:266px;top:1053px">
  <div style="position:absolute;left:0;right:0;top:8px">
    <div class="brand-ring" style="width:22px;height:22px"></div>
    <p class="brand" style="font-size:7px;margin:3px 0 0">ARRANGE YOUR<br>MONEY MATTERS</p>
    <p style="font-family:'Cinzel',serif;color:var(--gold);text-align:center;font-size:17px;line-height:1.35;margin:6px 0 0">THANK<br>YOU!</p>
  </div>
  <div style="position:absolute;left:9px;bottom:7px;display:flex;align-items:center;gap:4px;color:#fff">
    <span style="width:14px;height:14px;background:var(--blue);display:block"></span>
    <span style="font-size:4.8px;line-height:1.2"><b>WorkLoop · Deirdre Valcourt</b><br>arrangeyourmoneymatters@mailbox-example.net</span>
  </div>
</section>

</body>
</html>
```